QRV Law Letterhead

Want law firm letterhead - both in terms of a pdf file that I can use electronically as letterhead by adding it as a background - and in terms of a file that I can send to a company to create actual letterhead.
Industry/Entity Type
Law Firm
Font styles to use
Sans Serif
Requirements
Must have
- Should have the following information (you can decide where to place):
- My name - Corwin Haldane
- My email - corwin@qrvlawfirm.example
- My address - 2816 Pellworth Parkway 317-842
- San Jose, California 95742
- Website - www.qrvlawfirm.example
- Phone - 408-555-0187
- Fax - 408-555-0243
- The logo I attached
Nice to have
- I think I would prefer to have a black and white color scheme.
- I don't necessarily need a title after my name, but I have seen a few design submissions that include a generic title. The title I would use is "IP Litigator & Trademark Attorney"

```html
<!DOCTYPE html>
<html lang="en">
<head>
<meta charset="utf-8">
<title>QRV Law Letterhead</title>
<link href="https://fonts.googleapis.com/css2?family=Lato:wght@400;700&family=Open+Sans:wght@400;600&display=swap" rel="stylesheet">
<style>
  :root {
    --backdrop: #e6e6e6;
    --paper: #ffffff;
    --ink: #111111;
    --muted: #555555;
    --rule: #bdbdbd;
    --band: #0d0d0d;
    --band-text: #ffffff;
  }
  html, body {
    margin: 0;
    width: 1200px;
    height: 1200px;
    overflow: hidden;
    background: var(--backdrop);
  }
  .letterhead {
    position: absolute;
    left: 260px;
    top: 124px;
    width: 650px;
    height: 924px;
    background: var(--paper);
    box-shadow: 0 6px 22px rgba(0,0,0,0.25);
    overflow: hidden;
  }
  .brand {
    position: absolute;
    left: 50px;
    top: 66px;
    display: flex;
    align-items: center;
    gap: 10px;
  }
  .brand-mark {
    width: 40px;
    height: 40px;
    border-radius: 50%;
    background: var(--ink);
  }
  .brand-name {
    font-family: "Open Sans", sans-serif;
    font-weight: 600;
    font-size: 30px;
    color: var(--ink);
    letter-spacing: 0.5px;
  }
  .contact {
    position: absolute;
    left: 434px;
    top: 42px;
    padding-left: 14px;
    border-left: 1px solid var(--rule);
    height: 90px;
    font-family: "Lato", sans-serif;
    color: var(--muted);
    font-size: 9.5px;
    line-height: 13px;
  }
  .contact-name {
    margin: 0 0 6px;
    font-size: 12px;
    font-weight: 400;
    color: var(--ink);
    letter-spacing: -0.2px;
    text-transform: uppercase;
  }
  .contact-address { margin: 0 0 5px; }
  .contact-line {
    display: flex;
    align-items: center;
    gap: 5px;
    height: 15px;
  }
  .contact-line svg { width: 8px; height: 8px; fill: var(--ink); }
  .footer-band {
    position: absolute;
    left: 0;
    bottom: 0;
    width: 650px;
    height: 44px;
  }
  .footer-url {
    position: absolute;
    left: 500px;
    bottom: 11px;
    font-family: "Open Sans", sans-serif;
    font-weight: 600;
    font-size: 9px;
    color: var(--band-text);
  }
</style>
</head>
<body>
  <main class="letterhead">
    <header>
      <div class="brand">
        <span class="brand-mark"></span>
        <span class="brand-name">QRV Law</span>
      </div>
      <address class="contact">
        <p class="contact-name">Corwin Haldane</p>
        <p class="contact-address">2816 Pellworth Parkway<br>317-842, San Jose, California 95742</p>
        <div class="contact-line">
          <svg viewBox="0 0 10 10"><path d="M2 0.5 L3.5 2.8 L2.6 3.8 C3.2 5.2 4.8 6.8 6.2 7.4 L7.2 6.5 L9.5 8 L8.6 9.5 C4.5 9.5 0.5 5.5 0.5 1.4 Z"/></svg>
          <span>408-555-0187</span>
        </div>
        <div class="contact-line">
          <svg viewBox="0 0 10 10"><rect x="2.5" y="0.5" width="5" height="3"/><rect x="0.5" y="3.5" width="9" height="4" rx="1"/><rect x="2.5" y="6.5" width="5" height="3"/></svg>
          <span>408-555-0243</span>
        </div>
        <div class="contact-line">
          <svg viewBox="0 0 10 10"><path d="M0.5 2 H9.5 V8 H0.5 Z M0.5 2 L5 5.5 L9.5 2" stroke="#fff" stroke-width="0.8"/></svg>
          <span>corwin@qrvlawfirm.example</span>
        </div>
      </address>
    </header>
    <footer>
      <svg class="footer-band" viewBox="0 0 650 44" preserveAspectRatio="none" aria-hidden="true">
        <path d="M0 8 H430 C452 8 462 -1 500 -1 H650 V44 H0 Z" fill="var(--band)"/>
        <path d="M0 15 H432 C455 15 468 5 530 2" fill="none" stroke="#ffffff" stroke-width="3"/>
      </svg>
      <span class="footer-url">www.qrvlawfirm.example</span>
    </footer>
  </main>
</body>
</html>
```